political campaign lawn sign - Governor's Council in Massachuesetts

We are looking for a political lawn sign. We are running a campaign for Governor's Council in Massachusetts. This sign will be on the lawn of homes and businesses so people driving by will see it. It needs to be simple and bold. The last name is long so maybe it could say vote for Marty and then Kolbeck will be big a bold on the next line??
We need it to say:
Vote for Martin Kolbeck
Governor's Council.

Target Market(s)

local residents

Industry/Entity Type

Politcal Campaign

Font styles to use
Sans Serif
Other font styles liked:
• not sure what font but a modern looking one such as Helvetica, Arial, Sans Seri, sharp sans..

Colors
0054AA
0677BA
7BADD7
CADEEF
E8F1F8
00AB8E
00BBA5
67D7C9
C6EFE9
E9F9F6
FFF300
FFF600
FEFA6F
FFFEC7
FFFEE8

Requirements
Must have
• My name written out with a Capital D and R but lower case for every other letter so its Marty Kolbeck
Nice to have
• modern font , the Colors of the lawn sign should have Blue, Yellow and White something bold that will stand out
Should not have
• any maps of Massachusetts

```html
<!DOCTYPE html>
<html lang="en">
<head>
<meta charset="utf-8">
<title>Vote for Marty Kolbeck – Governor's Council Lawn Sign</title>
<link rel="stylesheet" href="https://fonts.googleapis.com/css2?family=Roboto+Condensed:wght@700&family=Roboto:wght@500&display=swap">
<style>
  :root {
    --sign-blue: #0054AA;
    --sign-yellow: #FFF300;
    --sign-white: #FFFFFF;
    --backdrop: #EEF1F4;
  }
  html, body {
    margin: 0;
    padding: 0;
    width: 720px;
    height: 1200px;
    overflow: hidden;
    background: var(--backdrop);
  }
  .lawn-sign {
    position: absolute;
    left: 0;
    top: 354px;
    width: 720px;
    height: 492px;
    display: block;
  }
  .panel-blue { fill: var(--sign-blue); }
  .panel-yellow { fill: var(--sign-yellow); }
  .sign-frame { fill: none; stroke: var(--sign-white); stroke-width: 8; }
  .headline-small,
  .headline-name {
    font-family: "Roboto Condensed", "Arial Narrow", sans-serif;
    font-weight: 700;
    fill: var(--sign-white);
  }
  .headline-small { font-size: 100px; }
  .headline-name { font-size: 182px; }
  .office-title {
    font-family: "Roboto Condensed", "Arial Narrow", sans-serif;
    font-weight: 700;
    font-size: 66px;
    fill: var(--sign-blue);
  }
  .campaign-url {
    font-family: "Roboto", Arial, sans-serif;
    font-weight: 500;
    font-size: 44px;
    fill: var(--sign-blue);
  }
</style>
</head>
<body>
  <svg class="lawn-sign" viewBox="0 0 720 492" xmlns="http://www.w3.org/2000/svg" aria-label="Campaign lawn sign: Vote for Marty Kolbeck, Governor's Council">
    <rect class="panel-blue" x="0" y="0" width="720" height="325"/>
    <rect class="panel-yellow" x="0" y="325" width="720" height="167"/>
    <polyline class="sign-frame" points="170,470 21,470 21,21 699,21 699,470 552,470"/>
    <text class="headline-small" x="360" y="116" text-anchor="middle" textLength="430" lengthAdjust="spacingAndGlyphs">Vote for Marty</text>
    <text class="headline-name" x="360" y="297" text-anchor="middle">Kolbeck</text>
    <text class="office-title" x="360" y="410" text-anchor="middle" textLength="590" lengthAdjust="spacingAndGlyphs">GOVERNER'S COUNCIL</text>
    <text class="campaign-url" x="361" y="479" text-anchor="middle" textLength="360" lengthAdjust="spacingAndGlyphs">voteformarty.net</text>
  </svg>
</body>
</html>
```